Harbor Print Studio gallery website

I need a Website for a gallery with a shopify integration or maybe even better also compatible with squarespace.
the website should have following riders: Künstler, Veranstaltungen, Shop, About Us.
some nice examples for inspiration of the website architecture are:
https://www.tarnelgalerie.com/
https://www.mossline-gallery.com/de/
https://zinnbergalerie.de/
It should be easy for us to make adaptations and fill the website with new content.
Attached there is the CI an logo for the brand.
Art Collectors,
artgallery
3 page

```html
<!DOCTYPE html>
<html lang="en">
<head>
<meta charset="utf-8">
<title>Harbor Print Studio</title>
<link href="https://fonts.googleapis.com/css2?family=Italiana&family=Montserrat:wght@300;400;500;600&display=swap" rel="stylesheet">
<style>
:root{
  --ink:#111;
  --muted:#666;
  --red:#e2140f;
  --deep:#14302e;
  --mist:#f2f0f0;
  --line:#cfcfcf;
  --white:#fff;
  --gold:#e6b800;
}
*{box-sizing:border-box;margin:0;padding:0}
html,body{width:1200px;height:5378px;overflow:hidden}
body{position:relative;font-family:'Montserrat',sans-serif;color:var(--ink);background:var(--white)}
.abs{position:absolute}
.display{font-family:'Italiana',serif;letter-spacing:.18em;font-weight:400}
a{color:inherit;text-decoration:none}

/* header */
.site-header{position:absolute;top:0;left:0;width:1200px;height:135px;background:var(--white)}
.nav-link{position:absolute;top:66px;font-size:11px;letter-spacing:.08em;text-transform:uppercase}
.brand{position:absolute;left:500px;top:76px;width:200px;text-align:center;font-size:17px;font-weight:400;color:#333;display:flex;align-items:center;justify-content:center;gap:6px}
.brand-square{width:10px;height:10px;background:var(--red)}
.header-icons{position:absolute;left:1008px;top:60px;display:flex;gap:16px}

/* hero */
.hero{position:absolute;top:135px;left:0;width:1200px;height:550px;background:linear-gradient(120deg,#d9a64a 0%,#c6462f 22%,#6a3fa0 45%,#1e7ca3 60%,#e07a2e 80%,#8b3a8f 100%)}
.hero-caption{position:absolute;left:0;top:376px;width:468px;height:111px;background:rgba(95,110,100,.82);color:var(--white)}
.hero-caption .bar{position:absolute;left:32px;top:20px;width:2px;height:70px;background:rgba(255,255,255,.7)}
.hero-caption h2{position:absolute;left:54px;top:30px;font-weight:400;font-size:23px;letter-spacing:.08em}
.hero-caption p{position:absolute;left:54px;top:68px;font-size:13px}
.hero-caption .go{position:absolute;left:396px;top:38px;width:40px;height:36px;background:var(--red);display:flex;align-items:center;justify-content:center}

/* gallery */
.section-title{font-size:48px}
.btn-dark{position:absolute;background:var(--ink);color:var(--white);font-size:14px;display:flex;align-items:center;justify-content:center}
.card{position:absolute;top:877px;width:273px;height:442px;background:var(--white);box-shadow:0 2px 10px rgba(0,0,0,.08);padding:12px}
.card .art{width:249px;height:292px}
.card .artist{margin-top:22px;font-size:13px;color:var(--muted)}
.card .title{margin-top:6px;font-size:17px;font-weight:500;letter-spacing:.06em}
.card .medium{margin-top:12px;font-size:11px;color:#999}
.card .more{margin-top:6px;font-size:13px;color:var(--red);display:flex;align-items:center;gap:6px}
.circle-btn{position:absolute;width:40px;height:40px;border-radius:50%;display:flex;align-items:center;justify-content:center}

/* about */
.about-art-wrap{position:absolute;left:0;top:1528px;width:600px;height:444px;background:var(--deep)}
.about-art{position:absolute;left:72px;top:50px;width:460px;height:345px;border:10px solid #d8c9a4;background:linear-gradient(150deg,#5b6a50,#c9c3a8 50%,#7c6a4c)}
.about-text{position:absolute;left:600px;top:1528px;width:600px;height:444px;background:var(--mist)}
.body-copy{font-size:12px;line-height:1.7;color:#555}

/* category */
.cat{position:absolute;overflow:hidden}
.cat span{position:absolute;left:28px;bottom:28px;color:var(--white);font-size:18px;letter-spacing:.1em;font-weight:500}
.cat::after{content:"";position:absolute;left:0;right:0;bottom:0;height:45%;background:linear-gradient(transparent,rgba(0,0,0,.55))}
.cat span{z-index:1}

/* event */
.event-art{position:absolute;left:0;top:2905px;width:600px;height:551px;background:linear-gradient(160deg,#c7d3d4,#e8e2d6 45%,#d97a3e 80%,#4f6f86)}
.event-panel{position:absolute;left:600px;top:2905px;width:600px;height:551px;background:var(--deep);color:var(--white)}
.meta-label{font-size:12px;font-weight:600}
.meta-value{font-size:12px;margin-top:6px;line-height:1.6;color:#ddd}

/* review */
.review{position:absolute;left:0;top:3970px;width:1200px;height:434px;background:var(--mist)}
.ghost{position:absolute;border:2px solid #fff}

/* contact */
.field{position:absolute;border:1px solid var(--line);font-size:11px;color:#777;padding:14px 16px}

/* footer */
.site-footer{position:absolute;left:0;top:5020px;width:1200px;height:358px;background:var(--deep);color:var(--white)}
.foot-col{position:absolute;top:78px}
.foot-col h4{font-size:13px;font-weight:400;letter-spacing:.05em;margin-bottom:18px}
.foot-col li{list-style:none;font-size:11.5px;color:#cfd6d5;line-height:23px}
.foot-divider{position:absolute;top:74px;width:2px;height:20px;background:var(--red)}
</style>
</head>
<body>

<header class="site-header">
  <a class="nav-link" style="left:140px">Künstler</a>
  <a class="nav-link" style="left:270px">Veranstaltungen</a>
  <div class="brand"><span class="brand-square"></span>Harbor Print Studio</div>
  <a class="nav-link" style="left:790px">About us</a>
  <a class="nav-link" style="left:902px">Shop</a>
  <div class="header-icons">
    <svg width="18" height="18" viewBox="0 0 18 18" fill="none" stroke="#555" stroke-width="1.5"><circle cx="7.5" cy="7.5" r="5.5"/><path d="M11.5 11.5l5 5"/></svg>
    <svg width="18" height="18" viewBox="0 0 24 24" fill="none" stroke="#555" stroke-width="1.6"><path d="M12 21s-8-5.3-8-11a4.5 4.5 0 0 1 8-2.8A4.5 4.5 0 0 1 20 10c0 5.7-8 11-8 11z"/></svg>
  </div>
</header>

<section class="hero" role="img" aria-label="Colourful painted close-up of an eye, featured artwork">
  <div class="hero-caption">
    <div class="bar"></div>
    <h2>GAZE OF THE INFINITE</h2>
    <p>Maren Solvik</p>
    <div class="go"><svg width="18" height="14" viewBox="0 0 18 14" fill="none" stroke="#fff" stroke-width="2"><path d="M1 7h15M10 1l6 6-6 6"/></svg></div>
  </div>
</section>

<section class="gallery">
  <h2 class="abs display section-title" style="left:140px;top:758px">GALLERY</h2>
  <p class="abs" style="left:140px;top:828px;font-size:14px;color:#555">Reesizing move editor bullet pencil</p>
  <a class="btn-dark" style="left:932px;top:794px;width:128px;height:42px">View All</a>

  <article class="card" style="left:140px">
    <div class="art" role="img" aria-label="Collage of a statue figure holding a red cup on yellow and teal" style="background:linear-gradient(90deg,#f0c43a,#f5c838 55%,#1f8c8a)"></div>
    <p class="artist">Ember Vale</p><h3 class="title">IRIDESCENT INSIGHT</h3><p class="medium">Painting</p>
    <a class="more">Learn more <svg width="14" height="8" viewBox="0 0 14 8" fill="none" stroke="#e2140f" stroke-width="1.3"><path d="M0 4h12M9 1l3 3-3 3"/></svg></a>
  </article>
  <article class="card" style="left:440px">
    <div class="art" role="img" aria-label="Abstract painting in violet and turquoise" style="background:linear-gradient(100deg,#8a4fc9,#5fc8e0 45%,#b65fd0 75%,#6a3bb0)"></div>
    <p class="artist">Ember Vale</p><h3 class="title">IRIDESCENT INSIGHT</h3><p class="medium">Painting</p>
    <a class="more">Learn more <svg width="14" height="8" viewBox="0 0 14 8" fill="none" stroke="#e2140f" stroke-width="1.3"><path d="M0 4h12M9 1l3 3-3 3"/></svg></a>
  </article>
  <article class="card" style="left:740px">
    <div class="art" role="img" aria-label="Collage portrait with flowers in muted tones" style="background:linear-gradient(160deg,#d9d3c8,#9a948a 60%,#d98a4a)"></div>
    <p class="artist">Ember Vale</p><h3 class="title">IRIDESCENT INSIGHT</h3><p class="medium">Painting</p>
    <a class="more">Learn more <svg width="14" height="8" viewBox="0 0 14 8" fill="none" stroke="#e2140f" stroke-width="1.3"><path d="M0 4h12M9 1l3 3-3 3"/></svg></a>
  </article>
  <article class="card" style="left:1040px">
    <div class="art" role="img" aria-label="Classical painting of figures in soft pink" style="background:linear-gradient(160deg,#f1e2dc,#e0b7a6)"></div>
    <p class="artist">Ember Vale</p><h3 class="title">IRIDESCENT INSIGHT</h3><p class="medium">Painting</p>
    <a class="more">Learn more <svg width="14" height="8" viewBox="0 0 14 8" fill="none" stroke="#e2140f" stroke-width="1.3"><path d="M0 4h12M9 1l3 3-3 3"/></svg></a>
  </article>

  <div class="abs" style="left:140px;top:1380px;width:780px;height:1px;background:var(--line)"></div>
  <div class="abs" style="left:140px;top:1379px;width:264px;height:3px;background:#333"></div>
  <div class="circle-btn" style="left:964px;top:1361px;border:1px solid #bbb"><svg width="8" height="12" viewBox="0 0 8 12" fill="none" stroke="#bbb" stroke-width="1.5"><path d="M7 1L2 6l5 5"/></svg></div>
  <div class="circle-btn" style="left:1020px;top:1361px;border:1.5px solid #222"><svg width="8" height="12" viewBox="0 0 8 12" fill="none" stroke="#222" stroke-width="1.5"><path d="M1 1l5 5-5 5"/></svg></div>
</section>

<section class="about">
  <div class="about-art-wrap"><div class="about-art" role="img" aria-label="Surreal framed artwork with a white horse and umbrella"></div></div>
  <div class="about-text">
    <h2 class="abs display section-title" style="left:85px;top:58px">ABOUT US</h2>
    <p class="abs body-copy" style="left:85px;top:134px;width:375px">Figma ipsum component variant main layer. Reesizing move editor bullet pencil. Connection draft arrow project align background component line. Opacity thumbnail team scale vertical figma stroke distribute vector. Frame scale boolean community object italic.</p>
    <p class="abs body-copy" style="left:85px;top:248px;width:375px">Opacity thumbnail team scale vertical figma stroke distribute vector. Frame scale boolean community object italic.</p>
    <a class="btn-dark" style="left:85px;top:344px;width:150px;height:42px">Read More</a>
  </div>
</section>

<section class="category">
  <h2 class="abs display section-title" style="left:0;top:2096px;width:1200px;text-align:center">BY CATEGORY</h2>
  <a class="cat" style="left:140px;top:2189px;width:294px;height:610px;background:linear-gradient(160deg,#f2c43a,#8c8c8c 50%,#d2332d 80%,#1f7a5a)" role="img" aria-label="Painting category, pop-art sculpture collage"><span>PAINTING</span></a>
  <a class="cat" style="left:451px;top:2189px;width:296px;height:297px;background:linear-gradient(140deg,#3aa0d0,#2a2a3a 50%,#e06a3a)" role="img" aria-label="Photography category, painted hands holding a camera"><span>PHOTOGRAPHY</span></a>
  <a class="cat" style="left:764px;top:2189px;width:296px;height:297px;background:linear-gradient(140deg,#e7dfd6,#6fa7a8 55%,#3a3a3a)" role="img" aria-label="Work on paper category, collage with leaves"><span>WORK ON PAPER</span></a>
  <a class="cat" style="left:451px;top:2502px;width:296px;height:297px;background:linear-gradient(140deg,#f2eef0,#d88fc0 45%,#5a9fd0)" role="img" aria-label="Sculpture category, colourful bust"><span>SCULPTURE</span></a>
  <a class="cat" style="left:764px;top:2502px;width:296px;height:297px;background:linear-gradient(140deg,#f4f0ec,#e8aaa6 50%,#c9753f)" role="img" aria-label="Printmaking category, abstract arch print"><span>PRINTMAKING</span></a>
</section>

<section class="event">
  <div class="event-art" role="img" aria-label="Collage of a figure among white flowers and orange foliage"></div>
  <div class="event-panel">
    <p class="abs" style="left:70px;top:66px;color:var(--red);font-size:14px">Next Event</p>
    <h2 class="abs display" style="left:70px;top:96px;font-size:31px;line-height:1.25">A SHOWCASE OF<br>TIMELESS ELEGANCE</h2>
    <p class="abs" style="left:70px;top:188px;width:390px;font-size:11.5px;line-height:1.7;color:#ccd">Join us at Harbor Print Studio gallery for an exquisite evening of artistic splendor as we unveil our latest collection, "Artistry Unveiled."</p>
    <div class="abs" style="left:70px;top:282px;display:flex;gap:10px">
      <svg width="16" height="16" viewBox="0 0 16 16" fill="none" stroke="#e2140f" stroke-width="1.4"><rect x="1" y="3" width="14" height="11" rx="2"/><path d="M1 7h14"/></svg>
      <div><p class="meta-label">Price</p><p style="font-size:19px;margin-top:6px">€ 79.00</p></div>
    </div>
    <div class="abs" style="left:255px;top:282px;display:flex;gap:10px">
      <svg width="14" height="18" viewBox="0 0 14 18" fill="none" stroke="#e2140f" stroke-width="1.4"><path d="M7 17s6-6 6-10A6 6 0 0 0 1 7c0 4 6 10 6 10z"/><circle cx="7" cy="7" r="2"/></svg>
      <div><p class="meta-label">Location</p><p class="meta-value">48 Quay Lane<br>Harborside, Portmere 20457</p></div>
    </div>
    <div class="abs" style="left:70px;top:360px;display:flex;gap:10px">
      <svg width="16" height="16" viewBox="0 0 16 16" fill="none" stroke="#e2140f" stroke-width="1.4"><rect x="1" y="2" width="14" height="13" rx="2"/><path d="M1 6h14M5 1v3M11 1v3"/></svg>
      <div><p class="meta-label">Date</p><p class="meta-value">March 15th, 2024</p></div>
    </div>
    <div class="abs" style="left:255px;top:360px;display:flex;gap:10px">
      <svg width="16" height="16" viewBox="0 0 16 16" fill="none" stroke="#e2140f" stroke-width="1.4"><circle cx="8" cy="8" r="7"/><path d="M8 4v4l3 2"/></svg>
      <div><p class="meta-label">Time</p><p class="meta-value">6:00 PM - 9:00 PM</p></div>
    </div>
    <a class="abs" style="left:70px;top:442px;width:390px;height:42px;background:var(--red);font-size:14px;display:flex;align-items:center;justify-content:center">Register Now</a>
  </div>
</section>

<section class="artist">
  <p class="abs" style="left:140px;top:3576px;font-size:14px">Artist</p>
  <h2 class="abs display" style="left:140px;top:3610px;font-size:42px">MAREN SOLVIK</h2>
  <p class="abs body-copy" style="left:140px;top:3678px;width:390px">Figma ipsum component variant main layer. Reesizing move editor bullet pencil. Connection draft arrow project align background component line. Opacity thumbnail team scale vertical figma stroke distribute vector. Frame scale boolean community object italic.</p>
  <p class="abs body-copy" style="left:140px;top:3782px;width:390px">Opacity thumbnail team scale vertical figma stroke distribute vector. Frame scale boolean community object italic.</p>
  <div class="abs" style="left:822px;top:3512px;width:200px;height:380px;border:2px solid var(--red);border-left:none;border-bottom:none"></div>
  <div class="abs" style="left:1012px;top:3528px;width:94px;height:160px;border:2px solid var(--red)"></div>
  <div class="abs" role="img" aria-label="Portrait of the artist in the studio" style="left:682px;top:3535px;width:378px;height:368px;background:linear-gradient(130deg,#c7733a,#3f4a55 45%,#9aa3a8 70%,#2a2e33)"></div>
  <div class="abs" style="left:1062px;top:3535px;width:2px;height:368px;background:var(--red)"></div>
  <div class="abs" style="left:682px;top:3851px;width:104px;height:52px;background:var(--red);display:flex;align-items:center;justify-content:center;gap:10px">
    <svg width="18" height="12" viewBox="0 0 18 12" fill="none" stroke="#fff" stroke-width="1.6"><path d="M17 6H2M6 1L1 6l5 5"/></svg>
    <svg width="18" height="12" viewBox="0 0 18 12" fill="none" stroke="#fff" stroke-width="1.6"><path d="M1 6h15M12 1l5 5-5 5"/></svg>
  </div>
</section>

<section class="review">
  <div class="ghost" style="left:36px;top:64px;width:60px;height:60px"></div>
  <div class="ghost" style="left:70px;top:100px;width:90px;height:210px"></div>
  <div class="ghost" style="left:1060px;top:254px;width:60px;height:60px"></div>
  <h2 class="abs display section-title" style="left:0;top:40px;width:1200px;text-align:center">REVIEW</h2>
  <div class="abs" role="img" aria-label="Reviewer portrait" style="left:566px;top:132px;width:68px;height:68px;border-radius:50%;background:linear-gradient(150deg,#d58a4a,#5a3a2a)"></div>
  <p class="abs" style="left:310px;top:228px;width:580px;text-align:center;font-size:14.5px;line-height:1.65;color:#444">Figma ipsum component variant main layer. Reesizing move editor bullet pencil. Connection draft arrow project align background component line. Opacity thumbnail team scale vertical figma stroke distribute vector. Frame scale boolean community object italic.</p>
  <div class="circle-btn" style="left:226px;top:250px;border:1px solid #bbb"><svg width="8" height="12" viewBox="0 0 8 12" fill="none" stroke="#bbb" stroke-width="1.5"><path d="M7 1L2 6l5 5"/></svg></div>
  <div class="circle-btn" style="left:934px;top:250px;border:1.5px solid #222"><svg width="8" height="12" viewBox="0 0 8 12" fill="none" stroke="#222" stroke-width="1.5"><path d="M1 1l5 5-5 5"/></svg></div>
  <p class="abs" style="left:0;top:346px;width:1200px;text-align:center;font-size:17px">Maren Solvik</p>
  <p class="abs" style="left:0;top:370px;width:1200px;text-align:center;font-size:16px;letter-spacing:3px;color:var(--gold)">★★★★★</p>
</section>

<section class="contact">
  <h2 class="abs display section-title" style="left:0;top:4486px;width:1200px;text-align:center">CONTACT US</h2>
  <p class="abs" style="left:330px;top:4568px;width:540px;text-align:center;font-size:14.5px;line-height:1.65;color:#555">Opacity thumbnail team scale vertical figma Opacity thumbnail team scale vertical figma</p>
  <div class="field" style="left:254px;top:4646px;width:338px;height:46px">Full name</div>
  <div class="field" style="left:608px;top:4646px;width:338px;height:46px">Phone number</div>
  <div class="field" style="left:254px;top:4710px;width:692px;height:46px">Email address</div>
  <div class="field" style="left:254px;top:4774px;width:692px;height:104px">Your message...</div>
  <a class="btn-dark" style="left:538px;top:4908px;width:124px;height:42px">Submit</a>
</section>

<footer class="site-footer">
  <div class="abs" style="left:120px;top:148px;width:190px;text-align:center;font-size:15px;display:flex;align-items:center;justify-content:center;gap:6px"><span style="width:9px;height:9px;background:var(--red)"></span>Harbor Print Studio</div>
  <div class="abs" style="left:176px;top:200px;display:flex;gap:8px">
    <span style="width:20px;height:20px;border:1px solid #8fa;border-color:#9aa8a6;border-radius:50%"></span>
    <span style="width:20px;height:20px;border:1px solid #9aa8a6;border-radius:50%"></span>
    <span style="width:20px;height:20px;border:1px solid #9aa8a6;border-radius:50%"></span>
  </div>
  <div class="abs" style="left:420px;top:60px;width:1px;height:170px;background:#3d5553"></div>
  <div class="foot-divider" style="left:632px"></div>
  <div class="foot-divider" style="left:832px"></div>
  <div class="foot-col" style="left:447px"><h4>QUICK LINKS</h4><ul><li>Künstler</li><li>About Us</li><li>Veranstaltungen</li><li>Shop</li><li>Contact Us</li></ul></div>
  <div class="foot-col" style="left:648px"><h4>BY CATEGORY</h4><ul><li>Painting</li><li>Photography</li><li>Sculpture</li><li>Work on Paper</li><li>Printmaking</li></ul></div>
  <div class="foot-col" style="left:847px"><h4>LEGAL</h4><ul><li>Privacy Policy</li><li>Terms and Conditions</li><li>Site Map</li></ul></div>
  <p class="abs" style="left:0;top:312px;width:1200px;text-align:center;font-size:11.5px;color:#cfd6d5">© 2024 All Rights Reserved | Harbor Print Studio</p>
</footer>

</body>
</html>
```